Haulage company, lets use ruby red white and some 3rd color for web design. and Alder Croft Transport logo

Target Market(s)

Transport industry

Industry/Entity Type

transport

Number of Pages Required

2 page

Requirements
Must have
• Logo

```html
<!DOCTYPE html>
<html lang="en">
<head>
<meta charset="utf-8">
<title>Alder Croft Transport – Web Design</title>
<link rel="stylesheet" href="https://fonts.googleapis.com/css2?family=Inter:wght@400;500;600;700;800&display=swap">
<style>
  :root {
    --ruby: #9e111f;
    --navy: #080a33;
    --white: #ffffff;
    --board: #f4f4f4;
    --accent: #6f7bdc;
    --muted: #8a8a96;
    --star: #f2b91c;
    --star-off: #d4d4d8;
    --line: #c9c9d3;
  }
  * { margin: 0; padding: 0; box-sizing: border-box; }
  html, body { width: 1200px; height: 1200px; overflow: hidden; }
  body {
    background: var(--board);
    font-family: "Inter", Arial, sans-serif;
    color: var(--navy);
    position: relative;
  }
  .abs { position: absolute; }

  /* Brand mark on the board */
  .brand {
    position: absolute; left: 50px; top: 40px; width: 290px;
    color: var(--ruby); font-weight: 800; text-align: right; line-height: 1;
  }
  .brand-name { font-size: 38px; letter-spacing: -0.5px; display: block; }
  .brand-sub { font-size: 22px; display: block; margin-top: 6px; }

  /* Page */
  .page {
    position: absolute; left: 376px; top: 43px; width: 462px; height: 1131px;
    background: var(--white); overflow: hidden;
  }

  /* Hero */
  .hero-panel { left: 233.5px; top: 0; width: 228.5px; height: 235px; background: var(--ruby); }
  .nav { left: 240px; top: 0; width: 222px; height: 16px; }
  .nav-link { position: absolute; top: 5.8px; font-size: 3.9px; line-height: 4.4px; color: var(--white); white-space: nowrap; }
  .nav-cta { position: absolute; left: 170px; top: 0.6px; width: 32.5px; height: 15px; background: var(--navy);
    color: var(--white); font-size: 3.9px; display: flex; align-items: center; justify-content: center; }
  .site-logo { left: 19.3px; top: 4px; color: var(--ruby); font-weight: 800; font-size: 5px; line-height: 1.1; }
  .dot-field-blue { background: rgba(111,123,220,0.12); }
  .dot-field-red { background: rgba(158,17,31,0.10); }
  .dot-field-light { background: rgba(255,255,255,0.10); }
  .eyebrow { left: 19.3px; top: 95px; font-size: 4.4px; font-weight: 700; color: var(--ruby); letter-spacing: 0.1px; }
  .hero-title { left: 19.3px; top: 103px; font-size: 13.6px; font-weight: 600; line-height: 18px; width: 220px; }
  .hero-title .hl { color: var(--ruby); font-size: 16.5px; }
  .hero-copy { left: 19.3px; top: 149px; width: 174px; font-size: 4.2px; line-height: 5.5px; }
  .btn-navy { background: var(--navy); color: var(--white); display: flex; align-items: center; justify-content: center; }
  .hero-btn { left: 19.3px; top: 186.3px; width: 38.5px; height: 15.5px; font-size: 4.4px; }
  .bar-red { background: var(--ruby); height: 4.4px; }
  .bar-white { background: var(--white); height: 3.6px; }
  .photo-road { background: linear-gradient(160deg, #6f9fd6 0%, #c9d9ea 40%, #8a9a8a 70%, #4d5a49 100%); }
  .photo-night { background: linear-gradient(170deg, #2a2f3a 0%, #4a4d55 45%, #c9c4bd 70%, #3c3a38 100%); }
  .photo-truck { background: linear-gradient(170deg, #b8c4d0 0%, #dfe3e7 40%, #9b2433 68%, #7e8288 100%); }

  /* About */
  .about-title { left: 270px; top: 300px; font-size: 12.4px; font-weight: 600; }
  .about-copy { left: 270px; top: 317px; width: 168px; font-size: 4.9px; line-height: 6.1px; }

  /* Services */
  .services { left: 0; top: 429.7px; width: 462px; height: 189.4px; background: var(--ruby); color: var(--white); }
  .section-title { position: absolute; left: 0; width: 100%; text-align: center; font-weight: 600; font-size: 11.6px; }
  .section-copy { position: absolute; left: 144px; width: 174px; text-align: center; font-size: 4.9px; line-height: 6.1px; }
  .service-card { position: absolute; top: 75.3px; width: 100.6px; height: 95px; border: 0.6px solid var(--white); padding: 6px 6.5px; }
  .service-card h3 { font-size: 7.2px; font-weight: 400; margin-bottom: 6px; white-space: nowrap; }
  .service-card p { font-size: 4.9px; line-height: 6.1px; }
  .read-more { position: absolute; left: 6.5px; top: 77.6px; width: 37px; height: 11px; font-size: 3.6px; gap: 3px; }
  .read-more svg { width: 5px; height: 5px; }

  /* Pricing */
  .pricing-title { top: 634px; font-size: 11.4px; color: var(--navy); }
  .plan { position: absolute; border: 0.6px solid var(--line); background: var(--white); padding: 11px 7.5px 0; }
  .plan-label { font-size: 4.6px; font-weight: 600; }
  .plan-price { color: var(--ruby); font-weight: 700; font-size: 10.5px; margin-top: 5px; }
  .plan-price small { font-size: 5px; font-weight: 600; }
  .plan-desc { font-size: 4.4px; line-height: 6.4px; margin-top: 8px; font-weight: 500; }
  .plan-list { list-style: none; margin-top: 6px; }
  .plan-list li { font-size: 3.8px; height: 9.6px; line-height: 9.6px; padding-left: 6px; position: relative; }
  .plan-list li::before { content: ""; position: absolute; left: 1.5px; top: 4.3px; width: 1.3px; height: 1.3px; border-radius: 50%; background: currentColor; }
  .plan-btn { position: absolute; left: 7.5px; height: 12.4px; font-size: 4.4px; gap: 3px; }
  .plan-btn svg { width: 4.4px; height: 4.4px; }
  .plan--popular { background: var(--navy); border-color: var(--navy); color: var(--white); padding-top: 9px; padding-left: 8px; }
  .plan--popular .plan-label span { color: var(--accent); }
  .plan--popular .plan-price { color: var(--white); font-size: 13.7px; margin-top: 4px; }
  .plan--popular .plan-price small { font-size: 6.4px; }
  .plan--popular .plan-desc { font-size: 5px; line-height: 7.8px; margin-top: 8px; }
  .plan--popular .plan-list li { font-size: 4.2px; height: 10.6px; line-height: 10.6px; }
  .plan--popular .plan-list li::before { top: 4.6px; }
  .btn-white { background: var(--white); color: var(--navy); display: flex; align-items: center; justify-content: center; }

  /* Testimonials */
  .review { position: absolute; top: 906px; width: 110.5px; height: 65px; border: 0.6px solid #6a6f8e; padding: 7px 6px; }
  .review-head { display: flex; align-items: center; gap: 5px; }
  .avatar { width: 15px; height: 15px; border-radius: 50%; background: linear-gradient(180deg, #e8e3dc, #3b3b44); }
  .rating { font-size: 10.5px; font-weight: 600; }
  .stars { font-size: 6px; letter-spacing: 3.4px; color: var(--star); }
  .stars .off { color: var(--star-off); }
  .review-quote { font-size: 4.6px; font-weight: 600; margin-top: 7px; }
  .review-text { font-size: 4.6px; line-height: 7.6px; color: var(--muted); margin-top: 11px; }
  .slider-arrow { position: absolute; top: 931.5px; width: 16.8px; height: 15.5px; background: #f1f1f4; display: flex; align-items: center; justify-content: center; }
  .slider-arrow svg { width: 11px; height: 11px; }
  .slider-dots { position: absolute; left: 207px; top: 979px; display: flex; gap: 4.8px; }
  .slider-dots span { width: 2.2px; height: 2.2px; border-radius: 50%; background: var(--navy); }

  /* Contact */
  .contact { left: 0; top: 1008.6px; width: 462px; height: 122.4px; background: var(--ruby); color: var(--white); }
  .contact-title { left: 55.3px; top: 14px; font-size: 11.4px; font-weight: 600; }
  .footer-col { position: absolute; top: 36px; font-size: 4.6px; }
  .footer-col h4 { font-weight: 600; font-size: 4.8px; margin-bottom: 4.6px; }
  .footer-col li { list-style: none; height: 10px; }
  .field { position: absolute; left: 306px; width: 100.6px; background: var(--white); color: var(--navy); font-size: 4px; padding: 4px 7.5px; }
  .submit { position: absolute; left: 306px; top: 84.4px; width: 100.6px; height: 13px; font-size: 4.4px; }
</style>
</head>
<body>

  <div class="brand">
    <span class="brand-name">Alder Croft</span>
    <span class="brand-sub">Transport</span>
  </div>

  <main class="page">
    <!-- Hero -->
    <div class="abs hero-panel"></div>
    <div class="abs site-logo">Alder Croft<br>Transport</div>
    <nav class="abs nav">
      <span class="nav-link" style="left:13px">Home</span>
      <span class="nav-link" style="left:42px">About</span>
      <span class="nav-link" style="left:70px">Services</span>
      <span class="nav-link" style="left:104px">Pricing</span>
      <span class="nav-link" style="left:135px">Testimonials</span>
      <span class="nav-cta">Contact</span>
    </nav>
    <div class="abs dot-field-blue" role="img" aria-label="Dotted grid decoration" style="left:0;top:37px;width:46.6px;height:44px"></div>
    <div class="abs eyebrow">CARGO SOLUTION</div>
    <h1 class="abs hero-title">Trust Your Cargo Shipping<br>to Reliable <span class="hl">Professionals.</span></h1>
    <p class="abs hero-copy">We are your trusted partner in delivering your goods safely and on time. With our modern fleet of trucks and experienced professional team, we offer customizable transportation solutions to meet your shipping needs. From local to national deliveries, we are committed to providing the best service to ensure your cargo reaches its destination safely.</p>
    <div class="abs btn-navy hero-btn">Contact us</div>
    <div class="abs bar-red" style="left:59px;top:197.5px;width:174.5px"></div>
    <div class="abs bar-red" style="left:82.6px;top:205.6px;width:151px"></div>
    <div class="abs bar-red" style="left:98px;top:214px;width:135.5px"></div>
    <div class="abs bar-white" style="left:233.5px;top:197.5px;width:228.5px"></div>
    <div class="abs bar-white" style="left:233.5px;top:206px;width:228.5px"></div>
    <div class="abs bar-white" style="left:233.5px;top:214.5px;width:228.5px"></div>
    <div class="abs dot-field-light" role="img" aria-label="Dotted grid decoration" style="left:287.5px;top:45px;width:111.5px;height:106px"></div>
    <div class="abs photo-road" role="img" aria-label="Photo of lorries parked beside a coastal road" style="left:305.5px;top:67px;width:65px;height:48px"></div>
    <div class="abs photo-night" role="img" aria-label="Photo of white lorries in a yard at night" style="left:341.5px;top:91.3px;width:101px;height:75.8px"></div>

    <!-- About -->
    <div class="abs photo-truck" role="img" aria-label="Photo of a red and white articulated lorry in a snowy yard" style="left:19.3px;top:248.4px;width:208px;height:155.3px"></div>
    <div class="abs dot-field-blue" role="img" aria-label="Dotted grid decoration" style="left:210px;top:364.5px;width:46.6px;height:42px"></div>
    <div class="abs dot-field-red" role="img" aria-label="Dotted grid decoration" style="left:409px;top:241.6px;width:46.6px;height:43px"></div>
    <h2 class="abs about-title">About Us</h2>
    <p class="abs about-copy">Lorem Ipsum is simply dummy text of the printing and typesetting industry. Lorem Ipsum has been the industry's standard dummy text ever since the 1500s, when an unknown printer took a galley of type and scrambled it to make a type specimen book. It has survived not only five centuries, but also the leap into electronic typesetting, remaining essentially unchanged.</p>

    <!-- Services -->
    <section class="abs services">
      <h2 class="section-title" style="top:11px">Our Services</h2>
      <p class="section-copy" style="top:28px">Lorem Ipsum is simply dummy text of the printing and typesetting industry. Lorem Ipsum has been the industry's standard dummy text ever since the 1500s, when an unknown printer took a galley of type and scrambled it to make a type specimen book.</p>

      <article class="service-card" style="left:19.3px">
        <h3>Local Delivery</h3>
        <p>Lorem Ipsum is simply dummy text of the printing and typesetting industry. Lorem Ipsum has been the industry's standard dummy text ever since the 1500s, when an unknown printer took a galley of type and scrambled it to make a type specimen book.</p>
        <div class="btn-navy read-more">Read More <svg viewBox="0 0 10 10"><circle cx="5" cy="5" r="4.3" fill="none" stroke="#fff" stroke-width="0.9"/><path d="M3 5h4M5.4 3.4 7 5 5.4 6.6" fill="none" stroke="#fff" stroke-width="0.9"/></svg></div>
      </article>
      <article class="service-card" style="left:126.7px">
        <h3>Interstate Shipping</h3>
        <p>Lorem Ipsum is simply dummy text of the printing and typesetting industry. Lorem Ipsum has been the industry's standard dummy text ever since the 1500s, when an unknown printer took a galley of type and scrambled it to make a type specimen book.</p>
        <div class="btn-navy read-more">Read More <svg viewBox="0 0 10 10"><circle cx="5" cy="5" r="4.3" fill="none" stroke="#fff" stroke-width="0.9"/><path d="M3 5h4M5.4 3.4 7 5 5.4 6.6" fill="none" stroke="#fff" stroke-width="0.9"/></svg></div>
      </article>
      <article class="service-card" style="left:234px">
        <h3>Specialized Freight</h3>
        <p>Lorem Ipsum is simply dummy text of the printing and typesetting industry. Lorem Ipsum has been the industry's standard dummy text ever since the 1500s, when an unknown printer took a galley of type and scrambled it to make a type specimen book.</p>
        <div class="btn-navy read-more">Read More <svg viewBox="0 0 10 10"><circle cx="5" cy="5" r="4.3" fill="none" stroke="#fff" stroke-width="0.9"/><path d="M3 5h4M5.4 3.4 7 5 5.4 6.6" fill="none" stroke="#fff" stroke-width="0.9"/></svg></div>
      </article>
      <article class="service-card" style="left:341.5px">
        <h3>Customized Logistics</h3>
        <p>Lorem Ipsum is simply dummy text of the printing and typesetting industry. Lorem Ipsum has been the industry's standard dummy text ever since the 1500s, when an unknown printer took a galley of type and scrambled it to make a type specimen book.</p>
        <div class="btn-navy read-more">Read More <svg viewBox="0 0 10 10"><circle cx="5" cy="5" r="4.3" fill="none" stroke="#fff" stroke-width="0.9"/><path d="M3 5h4M5.4 3.4 7 5 5.4 6.6" fill="none" stroke="#fff" stroke-width="0.9"/></svg></div>
      </article>
    </section>

    <!-- Pricing -->
    <h2 class="section-title pricing-title">Pricing</h2>

    <article class="plan" style="left:92px;top:673px;width:84.5px;height:138.5px">
      <div class="plan-label">Starter Pack</div>
      <div class="plan-price">$1,000<small>/year</small></div>
      <p class="plan-desc">Lorem ipsum dolor sit amet, consectetur adipiscing elit.</p>
      <ul class="plan-list"><li>Lorem ipsum dolor</li><li>Lorem ipsum dolor</li><li>Lorem ipsum dolor</li><li>Lorem ipsum dolor</li><li>Lorem ipsum dolor</li></ul>
      <div class="btn-navy plan-btn" style="top:118px;width:69.6px">Contact <svg viewBox="0 0 10 10"><path d="M1.5 5h7M5.5 2 8.5 5 5.5 8" fill="none" stroke="#fff" stroke-width="1.2"/></svg></div>
    </article>

    <article class="plan plan--popular" style="left:176.4px;top:658.3px;width:108px;height:160px">
      <div class="plan-label">Regular Pack <span>/ Popular</span></div>
      <div class="plan-price">$1,200<small>/year</small></div>
      <p class="plan-desc">Lorem ipsum dolor sit amet, consectetur adipiscing elit.</p>
      <ul class="plan-list"><li>Lorem ipsum dolor</li><li>Lorem ipsum dolor</li><li>Lorem ipsum dolor</li><li>Lorem ipsum dolor</li><li>Lorem ipsum dolor</li><li>Lorem ipsum dolor</li></ul>
      <div class="btn-white plan-btn" style="left:8px;top:139px;width:92.5px;height:13.7px">Contact <svg viewBox="0 0 10 10"><path d="M1.5 5h7M5.5 2 8.5 5 5.5 8" fill="none" stroke="#080a33" stroke-width="1.2"/></svg></div>
    </article>

    <article class="plan" style="left:284.4px;top:673px;width:85px;height:138.5px">
      <div class="plan-label">Advanced Pack</div>
      <div class="plan-price">$1,600<small>/year</small></div>
      <p class="plan-desc">Lorem ipsum dolor sit amet, consectetur adipiscing elit.</p>
      <ul class="plan-list"><li>Lorem ipsum dolor</li><li>Lorem ipsum dolor</li><li>Lorem ipsum dolor</li><li>Lorem ipsum dolor</li><li>Lorem ipsum dolor</li></ul>
      <div class="btn-navy plan-btn" style="top:118px;width:69.6px">Contact <svg viewBox="0 0 10 10"><path d="M1.5 5h7M5.5 2 8.5 5 5.5 8" fill="none" stroke="#fff" stroke-width="1.2"/></svg></div>
    </article>

    <!-- Testimonials -->
    <h2 class="section-title" style="top:845px;font-size:11.6px">See What Our Clients Have to Say</h2>
    <p class="section-copy" style="top:863px;color:var(--navy)">Lorem Ipsum is simply dummy text of the printing and typesetting industry. Lorem Ipsum has been the industry's standard dummy text ever since the 1500s, when an unknown printer took a galley of type and scrambled it to make a type specimen book.</p>

    <div class="slider-arrow" style="left:29px"><svg viewBox="0 0 12 12"><path d="M11 6H1.5M5.5 2 1.5 6l4 4" fill="none" stroke="#080a33" stroke-width="0.8"/></svg></div>
    <div class="slider-arrow" style="left:415.5px"><svg viewBox="0 0 12 12"><path d="M1 6h9.5M6.5 2l4 4-4 4" fill="none" stroke="#080a33" stroke-width="0.8"/></svg></div>

    <article class="review" style="left:55.3px">
      <div class="review-head"><div class="avatar" role="img" aria-label="Client portrait"></div><span class="rating">4.0</span><span class="stars">★★★★<span class="off">★</span></span></div>
      <p class="review-quote">“Lorem ipsum dolor sit amet”</p>
      <p class="review-text">Lorem ipsum dolor sit amet,<br>consectetur adipiscing elit.</p>
    </article>
    <article class="review" style="left:175.2px">
      <div class="review-head"><div class="avatar" role="img" aria-label="Client portrait"></div><span class="rating">4.0</span><span class="stars">★★★★<span class="off">★</span></span></div>
      <p class="review-quote">“Lorem ipsum dolor sit amet”</p>
      <p class="review-text">Lorem ipsum dolor sit amet,<br>consectetur adipiscing elit.</p>
    </article>
    <article class="review" style="left:295px">
      <div class="review-head"><div class="avatar" role="img" aria-label="Client portrait"></div><span class="rating">4.0</span><span class="stars">★★★★<span class="off">★</span></span></div>
      <p class="review-quote">“Lorem ipsum dolor sit amet”</p>
      <p class="review-text">Lorem ipsum dolor sit amet,<br>consectetur adipiscing elit.</p>
    </article>
    <div class="slider-dots"><span></span><span></span><span></span><span></span><span></span><span></span><span></span><span></span></div>

    <!-- Contact -->
    <footer class="abs contact">
      <h2 class="abs contact-title">Contact Us</h2>
      <div class="footer-col" style="left:55.3px">
        <h4>Company</h4>
        <ul><li>Home</li><li>About</li><li>Pricing</li><li>Testimonials</li></ul>
      </div>
      <div class="footer-col" style="left:126.7px">
        <h4>Services</h4>
        <ul><li>Local Delivery</li><li>Interstate Shipping</li><li>Specialized Freight</li><li>Customized Logistics</li></ul>
      </div>
      <div class="field" style="top:23.6px;height:12.4px">Your email</div>
      <div class="field" style="top:43.4px;height:34px">Enter your message</div>
      <div class="btn-navy submit">Submit</div>
    </footer>
  </main>

</body>
</html>
```